Social Media Graphics - Harbor Climb REVISED

Create 6-7 individual social media graphics (square size) to encourage folks to join our online course called:

The Lantern Ledger Plan
How to Launch a Multi-Million Business From Scratch
Sign Up Today!

IMPORTANT: Make the largest and most prominent text on the graphic be: How to Launch a Multi-Million Business From Scratch

For the color scheme of the graphics, let's try a blue color palette; make sure the graphics appeal to both men and women

Make sure each graphic contains 1 of the 3 pics attached (crop pic as needed); and make sure one of the graphics is all TEXT only.

Target Market(s)

men and women looking to start a business

Industry/Entity Type

Entrepreneurship

Colors
0054AA
0677BA
7BADD7
CADEEF
E8F1F8

Requirements
Must have
• All the text and use the 3 pics provided; one graphic can be all text; Simple, modern design that's easy to read

```html
<!DOCTYPE html>
<html lang="en">
<head>
<meta charset="utf-8">
<title>The Lantern Ledger Plan – Sign Up</title>
<link rel="stylesheet" href="https://fonts.googleapis.com/css2?family=Anton&family=Great+Vibes&family=Montserrat:ital,wght@0,700;0,800;1,800&display=swap">
<style>
  :root {
    --navy-deep: #05061c;
    --navy: #0a0c34;
    --blue: #2a6cf0;
    --blue-bright: #3b8dff;
    --sky: #1fb6ff;
    --ice: #e8f1f8;
    --mist: #cadeef;
    --white: #ffffff;
    --lime: #e9ff1c;
    --violet: #8a3cf0;
    --violet-soft: #b27bff;
    --pink: #e8306a;
  }
  * { margin: 0; padding: 0; box-sizing: border-box; }
  html, body { width: 1200px; height: 1200px; overflow: hidden; background: var(--navy-deep); }
  .poster {
    position: relative; width: 1200px; height: 1200px; overflow: hidden;
    background:
      radial-gradient(circle at 30% 92%, rgba(40,50,200,.45), transparent 40%),
      radial-gradient(circle at 0 0, rgba(90,30,160,.5), transparent 22%),
      linear-gradient(180deg, var(--navy-deep), var(--navy) 70%, #0c1060);
    font-family: "Montserrat", sans-serif;
  }
  .side-wave { position: absolute; inset: 0; z-index: 0; }
  .hosts-photo {
    position: absolute; left: 600px; top: 470px; width: 600px; height: 730px; z-index: 1;
    background:
      radial-gradient(ellipse 150px 300px at 230px 480px, rgba(232,48,106,.9), rgba(232,48,106,.5) 60%, transparent 100%),
      radial-gradient(ellipse 90px 110px at 250px 170px, rgba(40,25,35,.9), transparent 100%),
      radial-gradient(ellipse 160px 330px at 480px 430px, rgba(15,15,25,.95), rgba(15,15,25,.6) 65%, transparent 100%),
      radial-gradient(ellipse 70px 90px at 500px 90px, rgba(60,40,35,.9), transparent 100%);
  }
  .kicker {
    position: absolute; left: 72px; top: 111px; z-index: 2;
    color: var(--white); font-weight: 800; font-size: 33px; letter-spacing: 3px;
    transform: scaleX(1.34); transform-origin: left;
  }
  .headline {
    position: absolute; left: 80px; z-index: 2; font-family: "Anton", sans-serif; font-weight: 400;
    line-height: 1; white-space: nowrap; transform-origin: left;
    background: linear-gradient(115deg, var(--blue) 0%, var(--blue-bright) 40%, var(--white) 40.5%, var(--white) 100%);
    -webkit-background-clip: text; background-clip: text; color: transparent;
    -webkit-text-stroke: 2px rgba(255,255,255,.85);
  }
  .headline--million { top: 166px; font-size: 141px; transform: scaleX(.915); }
  .headline--business { top: 309px; font-size: 215px; transform: scaleX(.948); }
  .from {
    position: absolute; left: 130px; top: 535px; z-index: 3;
    font-family: "Great Vibes", cursive; font-size: 96px; line-height: 1; color: var(--white);
  }
  .scratch {
    position: absolute; left: 84px; top: 616px; z-index: 2;
    font-family: "Anton", sans-serif; font-size: 163px; line-height: 1; color: var(--lime);
    transform: scaleX(.84); transform-origin: left;
  }
  .plan-badge {
    position: absolute; left: 81px; top: 796px; width: 330px; height: 148px; z-index: 2;
    border-radius: 26px; border: 3px solid var(--violet-soft);
    background: linear-gradient(160deg, #5a1fb0 0%, #15103a 45%, #05061c 100%);
    transform: skewX(-4deg);
    display: flex; align-items: flex-start; justify-content: center; padding-top: 24px;
  }
  .plan-badge__name {
    font-weight: 800; font-style: italic; color: var(--white); font-size: 38px; letter-spacing: -1px;
    text-align: center; line-height: 1.05;
  }
  .plan-badge__tag {
    position: absolute; left: 165px; top: 915px; width: 263px; height: 49px; z-index: 3;
    border: 3px solid #0a0a0a; border-radius: 10px;
    background: linear-gradient(90deg, #050505 30%, #6f7a00 75%, var(--lime));
    color: var(--white); font-weight: 800; font-style: italic; font-size: 27px;
    display: flex; align-items: center; justify-content: center; transform: skewX(-4deg);
  }
  .cta {
    position: absolute; left: 78px; top: 1066px; z-index: 2;
    font-weight: 800; font-size: 38px; line-height: 1; letter-spacing: 10px; color: var(--white); white-space: nowrap;
  }
  .cta__accent { color: var(--lime); }
  .glow-icon {
    position: absolute; z-index: 4; width: 98px; height: 98px; border-radius: 24px;
    background: linear-gradient(145deg, var(--violet-soft), var(--violet));
    box-shadow: 0 0 30px rgba(180,110,255,.9), inset 0 0 10px rgba(255,255,255,.4);
    display: flex; align-items: center; justify-content: center;
  }
  .glow-icon svg { width: 54px; height: 54px; }
  .glow-icon--coins { left: 1036px; top: 119px; }
  .glow-icon--rupee { left: 928px; top: 340px; transform: rotate(15deg); width: 102px; height: 102px; }
  .glow-icon--rupee span { color: var(--white); font-weight: 800; font-size: 54px; }
  .glow-icon--exchange { left: 548px; top: 898px; width: 104px; height: 104px; transform: rotate(-10deg); }
  .glow-icon--growth { left: 993px; top: 1039px; width: 110px; height: 110px; transform: rotate(-12deg); }
</style>
</head>
<body>
<main class="poster">
  <svg class="side-wave" viewBox="0 0 1200 1200" aria-hidden="true">
    <defs>
      <linearGradient id="silk" x1="0" y1="0" x2="1" y2="1">
        <stop offset="0" stop-color="#e8f1f8"/>
        <stop offset=".5" stop-color="#cadeef"/>
        <stop offset="1" stop-color="#f4f8fb"/>
      </linearGradient>
      <linearGradient id="silk-fade" x1="0" y1="0" x2="0" y2="1">
        <stop offset="0" stop-color="#fff" stop-opacity="1"/>
        <stop offset=".75" stop-color="#fff" stop-opacity="1"/>
        <stop offset="1" stop-color="#fff" stop-opacity="0"/>
      </linearGradient>
      <mask id="silk-mask"><rect width="1200" height="1200" fill="url(#silk-fade)"/></mask>
      <linearGradient id="ribbon" x1="0" y1="0" x2="1" y2="0">
        <stop offset="0" stop-color="#3a2bff"/>
        <stop offset=".5" stop-color="#b04bff"/>
        <stop offset="1" stop-color="#5a2cff"/>
      </linearGradient>
    </defs>
    <g mask="url(#silk-mask)">
      <path d="M832 0 C930 180 995 420 1005 660 L1015 1200 L1200 1200 L1200 0 Z" fill="url(#silk)"/>
      <path d="M832 0 C930 180 995 420 1005 660 L1015 1200" fill="none" stroke="#1fb6ff" stroke-width="7"/>
    </g>
    <path d="M600 1080 C760 980 900 1120 1040 1050 S1180 1000 1200 1010" fill="none" stroke="url(#ribbon)" stroke-width="6" opacity=".9"/>
  </svg>

  <div class="hosts-photo" role="img" aria-label="Photo of the two course hosts smiling, a woman in a pink dress with arms crossed and a man in a dark jacket"></div>

  <p class="kicker">HOW TO LAUNCH A</p>
  <h1>
    <span class="headline headline--million">MULTI-MILLION</span>
    <span class="headline headline--business">BUSINESS</span>
  </h1>
  <p class="from">From</p>
  <p class="scratch">SCRATCH</p>

  <div class="plan-badge"><span class="plan-badge__name">LANTERN<br>LEDGER</span></div>
  <div class="plan-badge__tag">PLAN</div>

  <p class="cta">SIGN UP <span class="cta__accent">TODAY!</span></p>

  <div class="glow-icon glow-icon--coins">
    <svg viewBox="0 0 54 54" fill="#fff">
      <ellipse cx="20" cy="14" rx="13" ry="5"/>
      <ellipse cx="20" cy="24" rx="13" ry="5"/>
      <ellipse cx="20" cy="34" rx="13" ry="5"/>
      <circle cx="38" cy="33" r="11"/>
    </svg>
  </div>
  <div class="glow-icon glow-icon--rupee"><span>₹</span></div>
  <div class="glow-icon glow-icon--exchange">
    <svg viewBox="0 0 54 54" fill="none" stroke="#fff" stroke-width="4" stroke-linecap="round">
      <path d="M44 20 A19 19 0 1 0 44 36"/>
      <path d="M38 36 L45 36 L45 43"/>
      <text x="19" y="35" fill="#fff" stroke="none" font-family="Montserrat, sans-serif" font-weight="800" font-size="22">$</text>
    </svg>
  </div>
  <div class="glow-icon glow-icon--growth">
    <svg viewBox="0 0 54 54" fill="#fff">
      <rect x="8" y="34" width="6" height="12"/>
      <rect x="18" y="28" width="6" height="18"/>
      <rect x="28" y="32" width="6" height="14"/>
      <rect x="38" y="24" width="6" height="22"/>
      <path d="M6 26 L20 14 L30 22 L44 8" fill="none" stroke="#fff" stroke-width="4"/>
      <path d="M36 7 L46 6 L45 16 Z"/>
    </svg>
  </div>
</main>
</body>
</html>
```